Book Cover for Memoir: Sexual Assault and Traumatic Stress

I need a cover design for a memoir that is a victim's story of a sexual assault. I will need a print-on-demand cover, an eBook cover, and a 3D thumbnail image. The thumbnail and eBook cover will be used immediately, and the POD cover will be used in a few months with the full manuscript is ready. Therefore, I need an artist who is willing to make small adjustments if needed once the page count is set.

I have a image I have purchased that should give you an idea of the desired direction, but you can feel free to use your own images. I have attached some examples of book covers I like. I attached a color palette for fonts.

Overall Look: Fonts should be feminine and thin, but large to stand out. Look should be simple and elegant, and display and overall depressing feeling. There should be enough detail though to make it look professionally put together. Not TOO minimalistic.

I have also attached the Print Harbor templates if you choose to use those. If not, ensure there is an open place for the barcode on the bottom right.

Requirements
Must have
• Title: Beneath Quiet Rain
Subtitle: One Woman's Account of Fear, Guilt & Silence
Author: Dana Ruth Whitford
Audience: Mostly women 18-30
Quote (for the back): "I always thought I'd know how I'd react if I ever was raped. I was wrong. I've been wrong a lot lately."
Summary (back cover): When twenty-seven-year-old Dana Whitford wakes up with a gut-wrenching feeling, she has little memory of the horrifying events that occurred the night before. Days earlier, Dana was a spirited single mom who had abandoned her hometown to raise her daughter in the city and pursue her dreams. In the short months since Dana’s move to Seattle, she became the adored lover of a charismatic lawyer, started a new business, and finally felt life was going her way. So what happened to cause her to break?

In a gripping and heartbreaking narrative, Dana tells the true story of how her life unraveled from the traumatic events that took place that night and why what seems obvious to everyone else is impossible for Dana to believe. Beneath Quiet Rain is a chilling exploration of memory through trauma, trust in humanity, and a captivating story of strength and survival that appeals to the heart of fathers and mothers, sons and daughters, and men and women alike.
Nice to have
• BACK COVER: I'd like to have a photo on the back. This should depict the happy life of the main character before the sexual assault, and should be with her daughter. Or should be a nature scene that starts at the corner and blends into the rest of the cover. I have attached a possible image or you can use something you like.

```html
<!DOCTYPE html>
<html lang="en">
<head>
<meta charset="utf-8">
<title>Beneath Quiet Rain — Book Cover</title>
<link rel="stylesheet" href="https://fonts.googleapis.com/css2?family=Raleway:wght@100;200;300;600&family=Poiret+One&family=Oswald:wght@500;600&family=Open+Sans:wght@400&display=swap">
<style>
  :root{
    --back-navy:#1f1f33;
    --barcode-box:#e8e0de;
    --text-white:#ffffff;
    --text-muted:#a7a7b3;
    --text-dark:#2a2420;
    --text-faint:rgba(255,255,255,0.28);
    --hair-light:#d8a56a;
    --hair-mid:#b97a42;
    --hair-deep:#6b3f22;
    --skin-tone:#d9b094;
  }
  *{margin:0;padding:0;box-sizing:border-box;}
  html,body{width:1200px;height:854px;overflow:hidden;background:#ffffff;}
  .cover{position:relative;width:1200px;height:854px;overflow:hidden;}

  /* Back cover */
  .back{position:absolute;left:0;top:0;width:560px;height:854px;background:var(--back-navy);}
  .back-quote{
    position:absolute;left:0;top:52px;width:560px;text-align:center;
    font-family:"Poiret One","Raleway",sans-serif;font-size:22px;line-height:25px;
    letter-spacing:1.5px;color:var(--text-muted);text-transform:uppercase;
  }
  .back-quote .strong{color:var(--text-white);font-family:"Raleway",sans-serif;font-weight:300;}
  .back-photo{
    position:absolute;left:54px;top:175px;width:453px;height:271px;
    background:linear-gradient(120deg,#6f7d55 0%,#9aa07a 30%,#e2c9a6 55%,#7f88a8 85%,#5c6488 100%);
  }
  .back-summary{
    position:absolute;left:58px;top:478px;width:452px;
    font-family:"Open Sans",sans-serif;font-size:11.3px;line-height:14.2px;color:var(--text-white);
  }
  .back-summary p+p{margin-top:13px;}
  .back-summary .dropcap{font-size:17px;}
  .barcode-space{position:absolute;left:352px;top:709px;width:186px;height:104px;background:var(--barcode-box);}

  /* Photo spanning spine and front */
  .front-photo{
    position:absolute;left:560px;top:0;width:640px;height:854px;
    background:
      radial-gradient(ellipse 60% 45% at 70% 30%,rgba(217,176,148,0.75),transparent 70%),
      linear-gradient(100deg,var(--hair-deep) 0%,var(--hair-mid) 18%,var(--hair-light) 38%,#c48b55 60%,var(--hair-mid) 80%,var(--hair-deep) 100%);
  }

  /* Spine */
  .spine{position:absolute;left:560px;top:0;width:42px;height:854px;}
  .spine-title{
    position:absolute;left:21px;top:64px;transform-origin:0 0;transform:rotate(90deg) translateY(-50%);
    white-space:nowrap;font-family:"Raleway",sans-serif;font-size:30px;letter-spacing:3px;
    color:var(--text-white);text-transform:uppercase;line-height:1;
  }
  .spine-title .thin{font-weight:100;}
  .spine-title .bold{font-weight:300;}
  .spine-author{
    position:absolute;left:21px;top:662px;transform-origin:0 0;transform:rotate(90deg) translateY(-50%);
    white-space:nowrap;font-family:"Oswald",sans-serif;font-weight:600;font-size:17px;letter-spacing:0.5px;
    color:var(--text-dark);text-transform:uppercase;line-height:1;
  }

  /* Front cover */
  .front-title{
    position:absolute;left:712px;top:340px;width:460px;
    font-family:"Raleway",sans-serif;color:var(--text-white);text-transform:uppercase;
    font-size:82px;line-height:80px;letter-spacing:1px;
  }
  .front-title span{display:block;}
  .front-title .thin{font-weight:100;}
  .front-title .bold{font-weight:300;}
  .front-subtitle{
    position:absolute;left:712px;top:654px;width:470px;
    font-family:"Raleway",sans-serif;text-transform:uppercase;letter-spacing:1px;
  }
  .front-subtitle .lead{display:block;font-weight:600;font-size:21px;color:var(--text-dark);line-height:24px;}
  .front-subtitle .tail{display:block;font-weight:200;font-size:19px;color:var(--text-faint);line-height:24px;}
  .front-author{
    position:absolute;left:836px;top:789px;
    font-family:"Oswald",sans-serif;font-weight:500;font-size:20px;letter-spacing:0.5px;
    color:var(--text-white);text-transform:uppercase;
  }
</style>
</head>
<body>
<main class="cover">
  <section class="back">
    <blockquote class="back-quote">
      &ldquo;I always thought I&rsquo;d know<br>
      how I&rsquo;d react <span class="strong">if I ever was raped.</span><br>
      <span class="strong">I was wrong.</span><br>
      I&rsquo;ve been wrong a lot lately.<span class="strong">&rdquo;</span>
    </blockquote>

    <div class="back-photo" role="img" aria-label="Photo of a smiling mother hugging her young daughter outdoors"></div>

    <div class="back-summary">
      <p><span class="dropcap">W</span>hen twenty-seven-year-old Dana Whitford wakes up with a gut-wrenching feeling, she has little memory of the horrifying events that occurred the night before. Days earlier, Dana was a spirited single mom who had abandoned her hometown to raise her daughter in the city and pursue her dreams. In the short months since Dana&rsquo;s move to Seattle, she became the adored lover of a charismatic lawyer, started a new business, and finally felt life was going her way. So what happened to cause her to break?</p>
      <p>In a gripping and heartbreaking narrative, Dana tells the true story of how her life unraveled from the traumatic events that took place that night and why what seems obvious to everyone else is impossible for Dana to believe. Beneath Quiet Rain is a chilling exploration of memory through trauma, trust in humanity, and a captivating story of strength and survival that appeals to the heart of fathers and mothers, sons and daughters, and men and women alike.</p>
    </div>

    <div class="barcode-space"></div>
  </section>

  <div class="front-photo" role="img" aria-label="Close-up photo of a young woman with long windswept blonde hair"></div>

  <section class="spine">
    <div class="spine-title"><span class="thin">Beneath</span> <span class="bold">Quiet</span> <span class="thin">Rain</span></div>
    <div class="spine-author">Dana Ruth Whitford</div>
  </section>

  <section class="front">
    <h1 class="front-title">
      <span class="thin">Beneath</span>
      <span class="bold">Quiet</span>
      <span class="thin">Rain</span>
    </h1>
    <p class="front-subtitle">
      <span class="lead">One Woman&rsquo;s Account</span>
      <span class="tail">of Fear, Guilt &amp; Silence</span>
    </p>
    <p class="front-author">Dana Ruth Whitford</p>
  </section>
</main>
</body>
</html>
```